Web Design Project - Order A Moving Box for President Tebrin (the product (box) has been designed

Create a web site design for a politically oriented project with an e-commerce function.

The webite will most likely only need to be 4 or 5 pages at the most; with one of those being an order page.

Please email with any questions.

Designers,

We have uploaded a excel file containing content and ideas.
We don;t have the product art back yet but you can leave a space on the "THe Box" page and the "Home" page.
Please email is you have any questions.

Thanks,
Dane

Extension was added t allow more participation and updates from designers.

Target Market(s)

Conservation Voters, People who believe in the US Constitution, Capitalist, Entrepreneurs, Business Owners, Those who want to repeal TebrinCare

Industry/Entity Type

E-Commerce

Requirements
Must have
• Home Page
A Purpose and Mission Page (We have the content)
An order page

We have an outline of information that needs to be included.
You can email us directly at dane@pelbrook-nest.com and we can forward the sketches and type for the site.
Nice to have
• 1. Links to a few (2 or 3)video clips if possible (will provide)
2. Links to voter registration website (will provide link)
3. Links to 4 or 5 other websites.

```html
<!DOCTYPE html>
<html lang="en">
<head>
<meta charset="utf-8">
<title>Move Out Box — Home</title>
<link href="https://fonts.googleapis.com/css2?family=Cinzel:wght@400;700&family=Cabin+Condensed:wght@400;500&family=PT+Sans:wght@400;700&display=swap" rel="stylesheet">
<style>
:root{
  --bg:#000;
  --bar:#1c1c1c;
  --tab-active:#7a7a7a;
  --white:#fff;
  --panel:#ffffff;
  --heading-grey:#555;
  --body-grey:#5a5a5a;
  --gold:#c9960c;
  --rule:#cfcfcf;
  --btn:#7d7d7d;
  --nav-active:#9fc3e6;
}
*{box-sizing:border-box;margin:0;padding:0}
html,body{width:1200px;height:900px;overflow:hidden;background:var(--bg)}
body{position:relative;font-family:Arial,Helvetica,sans-serif}
.hero-glow{position:absolute;left:0;top:0;width:1200px;height:430px;
  background:
   linear-gradient(to bottom,rgba(0,0,0,0) 0%,rgba(0,0,0,.2) 60%,#000 100%),
   linear-gradient(90deg,#000 0%,#3a0606 5%,#7a1010 9%,#2a0820 12%,#5a1060 15%,#1a0a40 18%,#30106a 21%,#0a1030 25%,#000 32%,#000 68%,#0a1a0a 75%,#1a3a10 80%,#3a2a08 85%,#6a1a10 90%,#8a1a14 94%,#3a0606 97%,#000 100%);}
.top-nav{position:absolute;left:130px;top:0;width:960px;height:50px;background:rgba(40,40,40,.9);display:flex;align-items:center;padding-left:14px}
.top-nav a{font-family:'Cinzel',serif;color:var(--white);text-decoration:none;font-size:21px;margin-right:36px}
.top-nav a.active{color:var(--nav-active)}
.top-nav .arrow{width:0;height:0;border-left:13px solid #aaa;border-top:8px solid transparent;border-bottom:8px solid transparent;margin-right:12px}
.top-nav .phone{position:absolute;right:26px;top:14px;font-family:'PT Sans',sans-serif;color:var(--white);font-size:19px}
.hero-title{position:absolute;left:146px;top:64px;font-family:'Cinzel',serif;color:var(--white);font-weight:400;line-height:1}
.hero-title .big{font-size:43px;display:block;letter-spacing:1px;padding-left:4px}
.hero-title .sub{font-size:32px;display:block;margin-top:8px;line-height:34px;letter-spacing:1px}
.hero-list{position:absolute;left:164px;top:197px;list-style:none;font-family:'Cabin Condensed',sans-serif;color:var(--white);font-size:15px}
.hero-list li{height:25px;line-height:25px;display:flex;align-items:center}
.hero-list li svg{margin-right:6px}
.hero-list li.aside{font-style:italic;padding-left:62px}
.hero-art{position:absolute;left:590px;top:66px;width:501px;height:296px;background:linear-gradient(180deg,#4a3ce0 0%,#7a86f0 55%,#9ed27a 62%,#7cc05a 100%)}
.tab-band{position:absolute;left:0;top:426px;width:1200px;height:62px;background:var(--bar)}
.tab{position:absolute;top:426px;height:62px;font-family:'Cinzel',serif;color:var(--white);font-size:24px;line-height:80px}
.tab.active{left:130px;width:197px;background:var(--tab-active);text-align:center}
.tab.videos{left:543px}.tab.pages{left:902px}
.content{position:absolute;left:130px;top:488px;width:960px;height:348px;background:var(--panel)}
.intro h2{position:absolute;left:20px;top:26px;font-family:'PT Sans',sans-serif;font-weight:700;font-size:21px;color:var(--heading-grey)}
.intro .copy{position:absolute;left:21px;top:63px;width:590px;font-size:12.5px;line-height:24.2px;color:var(--body-grey)}
.copy .lg{font-size:15px}
.indent{padding-left:32px}.indent2{padding-left:56px}
.order-btn{position:absolute;left:490px;top:289px;width:128px;height:44px;background:var(--btn);border:3px solid #555;box-shadow:0 2px 4px rgba(0,0,0,.5);font-family:'Cinzel',serif;font-size:14px;font-weight:700;color:#222;text-align:center;line-height:38px}
.divider{position:absolute;left:637px;top:88px;width:1px;height:235px;background:var(--rule)}
.contact h3{position:absolute;left:702px;top:26px;font-family:'PT Sans',sans-serif;font-size:21px;color:var(--heading-grey)}
.contact .email{position:absolute;left:674px;top:108px;font-family:'PT Sans',sans-serif;font-size:21px;color:var(--gold)}
.contact .byphone{position:absolute;left:676px;top:236px;font-family:'PT Sans',sans-serif;font-size:21px;line-height:27px;color:var(--gold)}
.contact .icon-note{position:absolute;left:872px;top:80px}
.contact .icon-phone{position:absolute;left:870px;top:204px}
.footer{position:absolute;left:0;top:875px;width:1200px;text-align:center;font-family:'PT Sans',sans-serif;color:var(--white);font-size:13px}
</style>
</head>
<body>
<div class="hero-glow"></div>
<nav class="top-nav">
  <span class="arrow"></span>
  <a class="active" href="#">Home</a><a href="#">The Box</a><a href="#">The Purpose &amp; Mission</a><a href="#">Order</a>
  <span class="phone">888.555.0142</span>
</nav>
<h1 class="hero-title"><span class="big">Let Me Be Clear.</span><span class="sub">“The Buck Stops With<br>You” Mr. President</span></h1>
<ul class="hero-list">
  <li><svg width="10" height="10" viewBox="0 0 10 10"><path d="M1 5l3 3 5-7" stroke="#fff" stroke-width="2" fill="none"/></svg>This box will easily hold ALL of Corvan’s accomplishments.</li>
  <li class="aside">-- Oh wait, we forgot , there aren’t any!</li>
  <li><svg width="10" height="10" viewBox="0 0 10 10"><path d="M1 5l3 3 5-7" stroke="#fff" stroke-width="2" fill="none"/></svg>But it is too small to hold Lisette’s new $6,800$ shirt.</li>
  <li><svg width="10" height="10" viewBox="0 0 10 10"><path d="M1 5l3 3 5-7" stroke="#fff" stroke-width="2" fill="none"/></svg>It’s too small to hold all the gifts from the Brightvale executives.</li>
  <li><svg width="10" height="10" viewBox="0 0 10 10"><path d="M1 5l3 3 5-7" stroke="#fff" stroke-width="2" fill="none"/></svg>But it will hold all the souvenirs from his trip to Israel</li>
  <li class="aside">-- Oh we forgot, This President has never ever been!</li>
  <li><svg width="10" height="10" viewBox="0 0 10 10"><path d="M1 5l3 3 5-7" stroke="#fff" stroke-width="2" fill="none"/></svg>And of course, the box is much too small to contain his EGO</li>
</ul>
<div class="hero-art" role="img" aria-label="Cartoon of a moving truck outside the presidential residence, with the first family being packed up and a billboard pointing home"></div>

<div class="tab-band"></div>
<div class="tab active">The Box</div>
<div class="tab videos">Videos</div>
<div class="tab pages">Our Pages</div>

<main class="content">
  <section class="intro">
    <h2>Time To Tell Tebrin’s By Sending Them A Moving Box.</h2>
    <div class="copy">
      <p class="indent">Place your order and have this custom designed moving box sent directly to 1200</p>
      <p>Harrowgate Avenue <span class="lg">YES, the Capitol Residence.</span></p>
      <p class="indent">Lets male sure the Tebrins and the rest of the main stream media get the message that we are ready for some of that “HOPE &amp; CHANGE” he’s always talking about. It’s time to CHANGE the resident at the Capitol Residence and we HOPE they will be packed up and out come January 2013.</p>
      <p class="indent2" style="padding-left:56px">FOR US , it cant come some enough!!!</p>
      <p class="indent" style="padding-left:24px">For only $9.75 you can have a moving box sent to the Tebrins. Your box will be sent First Class Mail, which will also help prop up the failing Federal Parcel Service, in addition to sending your message of HOPE FOR CHANGE to the current Capitol Residence resident, your purchase of one box will provide enough food to feed a nutrious meal to 6 starving children.</p>
    </div>
    <div class="order-btn">Order a Box</div>
  </section>
  <div class="divider"></div>
  <aside class="contact">
    <h3>Contact Us Today</h3>
    <span class="email">Send an email</span>
    <svg class="icon-note" width="46" height="54" viewBox="0 0 46 54">
      <rect x="3" y="4" width="36" height="46" fill="#f4f4f4" stroke="#bbb"/>
      <path d="M14 38l22-30 5 4-22 30-6 2z" fill="#666"/>
    </svg>
    <span class="byphone">By Phone:<br>888.555.0187</span>
    <svg class="icon-phone" width="44" height="82" viewBox="0 0 44 82">
      <rect x="1" y="1" width="42" height="80" rx="7" fill="#111"/>
      <rect x="5" y="12" width="34" height="54" fill="#3a5a8a"/>
      <circle cx="22" cy="73" r="4" fill="#333"/>
    </svg>
  </aside>
</main>
<footer class="footer">All Rights Reserved</footer>
</body>
</html>
```